(3) Image Sliders for Wordpress Site

We need to update our WP slides on a corporate website. We are an IP communications solution provider to government and enterprises. Our website is www.velunor.com. You can see the existing sliders for size. I like crisp, professional-looking slides (NOT like the ones currently displayed). They shouldn't look like stock art/photos --- they should look original. They should also use current/new artistic methods (i.e. the "latest" concepts in design).

The Images should be JPG format, 946 x 376.

Use colors from logo on website, but don't completely restrict yourself. Photos are OK.

Slide Text:
Slide 1:
Main Message: "Creative solutions for government"
Bulleted text (use any kind of bullet or separator you want):
-Reduce FTE costs and eliminate capital expenses
-Dramatically improve community services
-Make government accessible for all constituents on all devices

Slide 2:
Main Message: "Corvane Systems Deployment"
-Take advantage of dramatic cost savings vs. going direct
-Leverage VeLUNOR's 13 years of experience
-Deploy On-Premises for optimal security, control and customization

Slide 3:
Main Message: "Enterprise Unified Communications"
-Revolutionize the way your people communicate and collaborate
-Realize instant cost savings by replacing multiple systems with one unified platform
-Bring everyone together, no matter where they are.

Hi Everyone I appreciate your submissions, but they are full of stock graphics and stuff I could have done..Looking for something more creative and unique to us. Since we're primarily a government/enterprise contractor, it doesn't have to be artsy or cute, but it does need to rise above the typical stock stuff i'm seeing. More information: -The Corvane Systems logo should go on the Corvane Systems-related slide -If you need more relevant logos or images let me know. Here are some slides that I like: http://brelmacraft.com/images/2014/0710-1/unslider.jpg http://brelmacraft.com/images/2014/0710-1/superslides.jpg http://www.tovelpikstudio.com/wp-content/uploads/2012/02/jquerysliders10b.jpg something like this with layered text for our gov slider, but NYC skyline: http://www.tovelpikstudio.com/wp-content/uploads/2012/02/jquerysliders18.jpg

Communications

```html
<!DOCTYPE html>
<html lang="en">
<head>
<meta charset="utf-8">
<title>Creative Solutions for Government</title>
<link rel="stylesheet" href="https://fonts.googleapis.com/css2?family=Open+Sans:wght@400;600;700;800&display=swap">
<style>
  :root {
    --sky-light: #8a8a8a;
    --sky-mid: #6f6f6f;
    --tower-dark: #2e2e2e;
    --accent-green: #8cc63f;
    --text-white: #ffffff;
    --button-blue: #0a63c6;
    --button-blue-dark: #084f9f;
    --dot-idle: rgba(255,255,255,0.45);
    --dot-active: #ffffff;
  }
  * { margin: 0; padding: 0; box-sizing: border-box; }
  html, body { width: 1200px; height: 477px; overflow: hidden; background: #5a5a5a; }
  .slide {
    position: relative;
    width: 1200px;
    height: 477px;
    overflow: hidden;
    font-family: "Open Sans", Arial, sans-serif;
    color: var(--text-white);
  }
  .slide-backdrop {
    position: absolute;
    inset: 0;
    background:
      linear-gradient(180deg, rgba(0,0,0,0) 40%, rgba(30,30,30,0.55) 100%),
      linear-gradient(90deg, var(--sky-light) 0%, var(--sky-mid) 55%, #555 85%, var(--tower-dark) 100%);
  }
  .pager {
    position: absolute;
    left: 34px;
    top: 42px;
    display: flex;
    gap: 7px;
  }
  .pager-dot {
    width: 11px;
    height: 11px;
    border-radius: 50%;
    background: var(--dot-idle);
  }
  .pager-dot.is-active { background: var(--dot-active); }
  .headline {
    position: absolute;
    left: 465px;
    top: 99px;
    padding-left: 19px;
    border-left: 6px solid var(--accent-green);
    font-weight: 800;
    font-size: 63px;
    line-height: 56px;
    letter-spacing: -2.2px;
    text-transform: uppercase;
    height: 110px;
    padding-top: 0;
  }
  .headline span { display: block; margin-top: -2px; }
  .benefits {
    position: absolute;
    left: 459px;
    top: 236px;
    list-style: none;
  }
  .benefit {
    display: flex;
    align-items: center;
    gap: 7px;
    height: 38px;
    font-size: 20px;
    font-weight: 400;
  }
  .benefit-icon { width: 21px; height: 21px; flex: none; }
  .cta-button {
    position: absolute;
    left: 455px;
    top: 364px;
    width: 186px;
    height: 43px;
    border-radius: 22px;
    background: var(--button-blue);
    border: 1px solid var(--button-blue-dark);
    color: var(--text-white);
    font-family: "Open Sans", Arial, sans-serif;
    font-weight: 700;
    font-size: 20px;
    display: flex;
    align-items: center;
    justify-content: center;
    text-decoration: none;
  }
</style>
</head>
<body>
  <section class="slide">
    <div class="slide-backdrop" role="img" aria-label="Grey upward view of downtown office towers against an overcast sky"></div>

    <div class="pager" aria-hidden="true">
      <span class="pager-dot"></span>
      <span class="pager-dot is-active"></span>
      <span class="pager-dot"></span>
    </div>

    <h1 class="headline"><span>Creative Solutions</span><span>for Government</span></h1>

    <ul class="benefits">
      <li class="benefit">
        <svg class="benefit-icon" viewBox="0 0 20 20" aria-hidden="true"><circle cx="10" cy="10" r="8.5" fill="none" stroke="#fff" stroke-width="2"/><path d="M5.8 10.2l3 3 5.6-6" fill="none" stroke="#fff" stroke-width="2.2" stroke-linecap="round" stroke-linejoin="round"/></svg>
        Reduce FTE costs and eliminate capital expenses
      </li>
      <li class="benefit">
        <svg class="benefit-icon" viewBox="0 0 20 20" aria-hidden="true"><circle cx="10" cy="10" r="8.5" fill="none" stroke="#fff" stroke-width="2"/><path d="M5.8 10.2l3 3 5.6-6" fill="none" stroke="#fff" stroke-width="2.2" stroke-linecap="round" stroke-linejoin="round"/></svg>
        Dramatically improve community services
      </li>
      <li class="benefit">
        <svg class="benefit-icon" viewBox="0 0 20 20" aria-hidden="true"><circle cx="10" cy="10" r="8.5" fill="none" stroke="#fff" stroke-width="2"/><path d="M5.8 10.2l3 3 5.6-6" fill="none" stroke="#fff" stroke-width="2.2" stroke-linecap="round" stroke-linejoin="round"/></svg>
        Make government accessible for all constituents on all devices
      </li>
    </ul>

    <a class="cta-button" href="#">Call to Action</a>
  </section>
</body>
</html>
```